Velsori Biotechnology needs a professional powerpoint design

We would like to re-design our powerpoint template(as attachment 1), it should be based on our current logo (as attachment 2). We hope the new powerpoint template could be more professional and like a biotechnology company with advanced technology.
Velsori Biotechnology is a contract development and manufacturing organization to provide high quality services to our clients in development, lead-in advanced technology and cGMP manufacturing of biopharmaceuticals from clinical to commercial manufacturing. We offers the advanced technology and services to become the best partner for clients from clinical to commercial manufacturing.
Reason: We would like to extend the deadline for this project so that designers can have more time to prepare, thanks.
Target Market(s)
Velsori Biotechnology is a contract development and manufacturing organization to provide high quality services to our clients in development, lead-in advanced technology and cGMP manufacturing of biopharmaceuticals from clinical to commercial manufacturing.
Velsori primary focus on development and manufacturing of glycoprotein pharmaceuticals against breast cancer, supplies KEP Taiwan with KEP-437 & KEP-438 for global clinical trials and commercialization in the future. Velsori offers the advanced technology and services to become the best partner for clients from clinical to commercial manufacturing.
Industry/Entity Type
Biotechnology
Requirements
Must have
- The new powerpoint design should based on our current logo.
Should not have
- The similar design with current powerpoint style. Please don't refer the design style of our current website http://www.velsori-example.com.tw/ as well, we will re-design it soon.

```html
<!DOCTYPE html>
<html lang="en">
<head>
<meta charset="utf-8">
<title>Velsori Biotechnology – Slide Template Overview</title>
<link href="https://fonts.googleapis.com/css2?family=Open+Sans:wght@300;400;600;700&display=swap" rel="stylesheet">
<style>
:root{
  --orange:#f7941d;
  --red:#e2492b;
  --green:#6db33f;
  --grey:#e8e8e8;
  --mid:#bdbdbd;
  --text:#333;
  --muted:#7a7a7a;
  --dark:#3d3d3d;
}
*{box-sizing:border-box}
html,body{margin:0;padding:0;overflow:hidden}
body{width:1200px;height:1009px;background:#3a3a3a;font-family:"Open Sans",sans-serif;color:var(--text)}
.deck{display:grid;grid-template-columns:repeat(4,300px);grid-template-rows:repeat(6,168.1667px);width:1200px;height:1009px}
.slide{position:relative;background:#fff;overflow:hidden}
.slide svg.art{position:absolute;inset:0;width:300px;height:168px}
.slide-title{position:absolute;left:13px;top:7px;margin:0;font-size:7px;font-weight:400;color:var(--text)}
.slide-sub{position:absolute;left:13px;top:17px;font-size:3px;color:var(--muted)}
.brand{position:absolute;right:11px;top:8px;font-size:6px;font-weight:700;color:var(--orange);letter-spacing:.3px;display:flex;align-items:center;gap:2px}
.brand::before{content:"";width:4px;height:4px;border-radius:50%;background:var(--orange)}
.foot{position:absolute;left:0;right:0;bottom:0;height:7px;border-top:1.4px solid var(--orange)}
.foot .url{position:absolute;left:0;top:0;height:5.6px;width:58px;background:var(--orange);color:#fff;font-size:3px;line-height:5.6px;padding-left:4px;clip-path:polygon(0 0,100% 0,90% 100%,0 100%)}
.foot .copy{position:absolute;right:8px;top:.5px;font-size:3px;color:var(--muted)}
.foot .dot{position:absolute;left:148px;top:1px;width:4px;height:4px;border:.4px solid var(--mid);border-radius:50%}
.tx{position:absolute;font-size:2.8px;line-height:1.4;color:var(--muted);margin:0}
.hd{position:absolute;font-size:3.6px;font-weight:700;color:var(--text);margin:0}
.photo{position:absolute}
.avatar{position:absolute;border-radius:50%;background:linear-gradient(#cfcfcf,#9c9c9c)}
.contact{background:var(--dark)}
.contact .top{position:absolute;left:0;right:0;top:0;height:88px;background:linear-gradient(135deg,#e85a35,#d9472a)}
.mapslide{background:#4a4a4a}
.blank{background:#3a3a3a}
</style>
</head>
<body>
<main class="deck">

<!-- 27 Infographic circle -->
<section class="slide">
  <h2 class="slide-title">Infographic Circle</h2><div class="slide-sub">Your Subtitle Goes Here</div><div class="brand">VELSORI</div>
  <svg class="art" viewBox="0 0 300 168" font-family="Open Sans, sans-serif">
    <circle cx="68" cy="95" r="36" fill="none" stroke="#ececec" stroke-width="24"/>
    <circle cx="68" cy="95" r="52" fill="none" stroke="var(--orange)" stroke-width="8" stroke-dasharray="70 8 60 8 40 8 60 8" transform="rotate(-160 68 95)"/>
    <circle cx="68" cy="95" r="43" fill="none" stroke="var(--red)" stroke-width="5" stroke-dasharray="20 250" transform="rotate(-165 68 95)"/>
    <circle cx="68" cy="95" r="14" fill="none" stroke="var(--red)" stroke-width="5"/>
    <g font-size="4.5" font-weight="700" fill="var(--text)">
      <text x="43" y="55">32%</text><text x="82" y="53">37%</text><text x="20" y="87">30%</text>
      <text x="90" y="96">20%</text><text x="96" y="110">20%</text><text x="90" y="122">20%</text>
      <text x="36" y="120">27%</text><text x="60" y="128">25%</text>
    </g>
    <g font-size="3.6" font-weight="700" fill="var(--text)">
      <text x="166" y="45">HEADING HERE</text><text x="226" y="45">HEADING HERE</text>
      <text x="166" y="72">HEADING HERE</text><text x="226" y="72">HEADING HERE</text>
      <text x="166" y="99">HEADING HERE</text><text x="226" y="99">HEADING HERE</text>
      <text x="166" y="126">HEADING HERE</text><text x="226" y="126">HEADING HERE</text>
    </g>
    <g font-size="2.5" fill="var(--muted)">
      <text x="166" y="50">SHORT NOTE ON THIS TOPIC</text><text x="226" y="50">SHORT NOTE ON THIS TOPIC</text>
      <text x="166" y="77">SHORT NOTE ON THIS TOPIC</text><text x="226" y="77">SHORT NOTE ON THIS TOPIC</text>
      <text x="166" y="104">SHORT NOTE ON THIS TOPIC</text><text x="226" y="104">SHORT NOTE ON THIS TOPIC</text>
      <text x="166" y="131">SHORT NOTE ON THIS TOPIC</text><text x="226" y="131">SHORT NOTE ON THIS TOPIC</text>
    </g>
  </svg>
  <footer class="foot"><span class="url">velsori-example.com.tw</span><span class="dot"></span><span class="copy">© 2016 Velsori Biotechnology Inc. › 27</span></footer>
</section>

<!-- 28 Pie chart -->
<section class="slide">
  <h2 class="slide-title">Pie Chart</h2><div class="slide-sub">Your Subtitle Goes Here</div><div class="brand">VELSORI</div>
  <svg class="art" viewBox="0 0 300 168" font-family="Open Sans, sans-serif">
    <circle cx="92" cy="90" r="40" fill="#ececec"/>
    <circle cx="92" cy="90" r="20" fill="none" stroke="var(--orange)" stroke-width="40" stroke-dasharray="40 126" transform="rotate(-125 92 90)"/>
    <circle cx="96" cy="88" r="20" fill="none" stroke="var(--red)" stroke-width="40" stroke-dasharray="24 126" transform="rotate(-10 96 88)"/>
    <circle cx="96" cy="94" r="20" fill="none" stroke="var(--green)" stroke-width="40" stroke-dasharray="14 126" transform="rotate(58 96 94)"/>
    <text x="70" y="106" font-size="10" fill="var(--muted)">45%</text>
    <text x="86" y="68" font-size="6" fill="#fff" font-weight="700">35%</text>
    <text x="116" y="85" font-size="5" fill="#fff">20%</text>
    <text x="113" y="104" font-size="4" fill="#fff">10%</text>
  </svg>
  <h3 class="hd" style="left:174px;top:38px;font-weight:600">Lorem Ipsum Penatibus</h3>
  <p class="tx" style="left:174px;top:49px;width:110px">Our team builds each step with care, from early cell line work to final fill, so clients move from trial to market with one steady partner at every stage.</p>
  <p class="tx" style="left:174px;top:75px;width:110px">Clear methods and tested systems keep each batch on track and ready.</p>
  <h3 class="hd" style="left:174px;top:95px;font-weight:600">Phasellus ullamcorper</h3>
  <p class="tx" style="left:174px;top:104px;width:110px">• Present adipiscing<br>• Integer ante arcu<br>• Accumsan a consectetur<br>• Present adipiscing<br>• Integer arcu<br>• Phasellus ullamcorper</p>
  <footer class="foot"><span class="url">velsori-example.com.tw</span><span class="dot"></span><span class="copy">© 2016 Velsori Biotechnology Inc. › 28</span></footer>
</section>

<!-- 29 Bar, line & table -->
<section class="slide">
  <h2 class="slide-title">Bar, Line &amp; Table Charts</h2><div class="slide-sub">Your Subtitle Goes Here</div><div class="brand">VELSORI</div>
  <svg class="art" viewBox="0 0 300 168" font-family="Open Sans, sans-serif">
    <g stroke="#eee" stroke-width=".4"><line x1="18" y1="35" x2="130" y2="35"/><line x1="18" y1="50" x2="130" y2="50"/><line x1="18" y1="65" x2="130" y2="65"/><line x1="18" y1="80" x2="130" y2="80"/></g>
    <polyline points="22,58 42,40 62,38 82,48 102,66 122,36" fill="none" stroke="var(--orange)" stroke-width=".8"/>
    <polyline points="22,54 42,44 62,54 82,44 102,58 122,54" fill="none" stroke="var(--red)" stroke-width=".8"/>
    <g font-size="2.4" fill="var(--muted)"><text x="20" y="87">VALUE 01</text><text x="47" y="87">VALUE 02</text><text x="74" y="87">VALUE 03</text><text x="101" y="87">VALUE 04</text></g>
    <g stroke="#eee" stroke-width=".4"><line x1="18" y1="100" x2="130" y2="100"/><line x1="18" y1="115" x2="130" y2="115"/><line x1="18" y1="130" x2="130" y2="130"/><line x1="18" y1="145" x2="130" y2="145"/></g>
    <polyline points="22,140 32,136 42,128 52,132 62,120 72,116 82,120 92,112 102,104 112,102" fill="none" stroke="var(--orange)" stroke-width=".8"/>
    <g stroke="#eee" stroke-width=".4"><line x1="150" y1="35" x2="285" y2="35"/><line x1="150" y1="50" x2="285" y2="50"/><line x1="150" y1="65" x2="285" y2="65"/></g>
    <g fill="var(--red)"><rect x="160" y="37" width="5" height="43"/><rect x="187" y="36" width="5" height="44"/><rect x="214" y="42" width="5" height="38"/><rect x="241" y="36" width="5" height="44"/></g>
    <g fill="var(--orange)"><rect x="166" y="40" width="5" height="40"/><rect x="193" y="46" width="5" height="34"/><rect x="220" y="50" width="5" height="30"/><rect x="247" y="46" width="5" height="34"/></g>
    <line x1="150" y1="80" x2="285" y2="80" stroke="#ccc" stroke-width=".4"/>
    <text x="152" y="104" font-size="7" font-weight="700" fill="var(--text)">Heading Here</text>
    <g font-size="3" fill="var(--text)"><text x="152" y="115">Content A</text><text x="210" y="115">Content C</text><text x="152" y="136">Content B</text><text x="210" y="136">Content D</text></g>
    <g font-size="2.4" fill="var(--muted)"><text x="152" y="119">Brief note for this item</text><text x="210" y="119">Brief note for this item</text><text x="152" y="140">Brief note for this item</text><text x="210" y="140">Brief note for this item</text></g>
  </svg>
  <footer class="foot"><span class="url">velsori-example.com.tw</span><span class="dot"></span><span class="copy">© 2016 Velsori Biotechnology Inc. › 29</span></footer>
</section>

<!-- 30 Line graph -->
<section class="slide">
  <h2 class="slide-title">Line Graph Chart</h2><div class="slide-sub">Your Subtitle Goes Here</div><div class="brand">VELSORI</div>
  <h3 class="hd" style="left:13px;top:44px;font-weight:400;font-size:4px">Your Title Goes Here</h3>
  <p class="tx" style="left:13px;top:55px;width:120px">Our team builds each step with care, from early cell line work to final fill, so clients move from trial to market with one steady partner. Clear methods and tested systems keep each batch on track and ready for review.</p>
  <p class="tx" style="left:13px;top:92px;width:120px">Our team builds each step with care, from early cell line work to final fill, so clients move from trial to market with one steady partner. Clear methods and tested systems keep each batch on track and ready for review by the team.</p>
  <svg class="art" viewBox="0 0 300 168" font-family="Open Sans, sans-serif">
    <g stroke="#eee" stroke-width=".4"><line x1="158" y1="45" x2="288" y2="45"/><line x1="158" y1="60" x2="288" y2="60"/><line x1="158" y1="75" x2="288" y2="75"/><line x1="158" y1="90" x2="288" y2="90"/><line x1="158" y1="105" x2="288" y2="105"/><line x1="158" y1="120" x2="288" y2="120"/></g>
    <polyline points="162,95 170,70 178,90 186,60 194,98 202,72 210,88 218,64 226,95 234,80 242,70 250,92 258,85 266,78 274,84 282,82" fill="none" stroke="var(--orange)" stroke-width=".7"/>
    <polyline points="162,80 170,90 178,75 186,100 194,78 202,96 210,70 218,92 226,74 234,98 242,82 250,76 258,94 266,86 274,88 282,96" fill="none" stroke="var(--red)" stroke-width=".6"/>
    <g font-size="2.3" fill="var(--muted)"><text x="158" y="127">AB CD EF GH IJ KL MN OP QR ST UV WX YZ</text></g>
  </svg>
  <footer class="foot"><span class="url">velsori-example.com.tw</span><span class="dot"></span><span class="copy">© 2016 Velsori Biotechnology Inc. › 30</span></footer>
</section>

<!-- 31 Tables chart & contents -->
<section class="slide">
  <h2 class="slide-title">Tables Chart &amp; Contents</h2><div class="slide-sub">Your Subtitle Goes Here</div><div class="brand">VELSORI</div>
  <p class="tx" style="left:22px;top:32px;width:92px"><b style="color:var(--text)">TITLE HERE</b><br>Our team builds each step with care, from early cell work to final fill, so clients move from trial to market with one steady partner.</p>
  <p class="tx" style="left:152px;top:32px;width:48px"><b style="color:var(--text)">TITLE HERE</b><br>Clear methods keep each batch on track and ready.</p>
  <p class="tx" style="left:207px;top:32px;width:48px"><b style="color:var(--text)">TITLE HERE</b><br>Clear methods keep each batch on track and ready.</p>
  <svg class="art" viewBox="0 0 300 168" font-family="Open Sans, sans-serif">
    <g stroke="#eee" stroke-width=".4"><line x1="28" y1="70" x2="150" y2="70"/><line x1="28" y1="85" x2="150" y2="85"/><line x1="28" y1="100" x2="150" y2="100"/><line x1="28" y1="115" x2="150" y2="115"/><line x1="28" y1="130" x2="150" y2="130"/><line x1="28" y1="145" x2="150" y2="145"/></g>
    <g stroke="#999" stroke-width=".4"><line x1="42" y1="90" x2="42" y2="120"/><line x1="62" y1="84" x2="62" y2="122"/><line x1="82" y1="76" x2="82" y2="112"/><line x1="102" y1="80" x2="102" y2="118"/><line x1="122" y1="88" x2="122" y2="126"/></g>
    <rect x="39" y="96" width="6" height="14" fill="var(--orange)"/><rect x="59" y="102" width="6" height="9" fill="var(--red)"/>
    <rect x="79" y="82" width="6" height="9" fill="var(--red)"/><rect x="99" y="84" width="6" height="14" fill="var(--orange)"/><rect x="119" y="100" width="6" height="12" fill="var(--orange)"/>
    <g font-size="2.4" fill="var(--muted)"><text x="55" y="152">TITLE 01</text><text x="75" y="152">TITLE 02</text><text x="95" y="152">TITLE 03</text><text x="115" y="152">TITLE 04</text></g>
  </svg>
  <h3 class="hd" style="left:160px;top:80px;font-size:3.2px;font-weight:600">Your Title Goes Here</h3>
  <p class="tx" style="left:160px;top:88px;width:110px">Our team builds each step with care, from early cell line work to final fill, so clients move from trial to market with one steady partner.</p>
  <p class="tx" style="left:160px;top:108px;width:110px">Clear methods and tested systems keep each batch on track. Every run is checked, logged and shared with the client team in plain terms.</p>
  <footer class="foot"><span class="url">velsori-example.com.tw</span><span class="dot"></span><span class="copy">© 2016 Velsori Biotechnology Inc. › 31</span></footer>
</section>

<!-- 32 Editable pie -->
<section class="slide">
  <h2 class="slide-title">Editable Pie Chart</h2><div class="slide-sub">Your Subtitle Goes Here</div><div class="brand">VELSORI</div>
  <svg class="art" viewBox="0 0 300 168" font-family="Open Sans, sans-serif">
    <g transform="rotate(-90 75 88)" fill="none" stroke-width="18">
      <circle cx="75" cy="88" r="38" stroke="var(--orange)"/>
      <circle cx="75" cy="88" r="38" stroke="var(--red)" stroke-dasharray="53 186" stroke-dashoffset="-150"/>
      <circle cx="75" cy="88" r="38" stroke="#f5a93a" stroke-dasharray="22 216" stroke-dashoffset="-203"/>
      <circle cx="75" cy="88" r="38" stroke="var(--red)" stroke-dasharray="14 226" stroke-dashoffset="-225"/>
    </g>
    <g font-size="3" fill="#fff"><text x="101" y="94">63%</text><text x="42" y="99">22%</text><text x="47" y="72">13%</text><text x="64" y="57">9%</text></g>
    <g font-size="2.2" fill="var(--muted)"><text x="42" y="141">● 1st Qtr  ● 2nd Qtr  ● 3rd Qtr  ● 4th Qtr</text></g>
    <text x="152" y="119" font-size="15" font-weight="700" fill="var(--text)">63%</text>
  </svg>
  <h3 class="hd" style="left:152px;top:46px;font-size:5.6px">Your Heading Goes Here</h3>
  <p class="tx" style="left:152px;top:56px;width:135px">Our team builds each step with care, from early cell line work to final fill, so clients move from trial to market with one steady partner. Clear methods and tested systems keep each batch on track and ready.</p>
  <p class="tx" style="left:190px;top:105px;font-size:4.2px;line-height:1.2">Heading<br>Title Goes Here</p>
  <p class="tx" style="left:152px;top:126px;width:135px">Our team builds each step with care, from early cell line work to final fill, so clients move from trial to market with one steady partner.</p>
  <footer class="foot"><span class="url">velsori-example.com.tw</span><span class="dot"></span><span class="copy">© 2016 Velsori Biotechnology Inc. › 32</span></footer>
</section>

<!-- 33 Circle chart -->
<section class="slide">
  <h2 class="slide-title">Circle Chart</h2><div class="slide-sub">Your Subtitle Goes Here</div><div class="brand">VELSORI</div>
  <svg class="art" viewBox="0 0 300 168" font-family="Open Sans, sans-serif">
    <g fill="none" stroke-width="3.5">
      <circle cx="48" cy="62" r="17" stroke="#eee"/><circle cx="48" cy="62" r="17" stroke="var(--orange)" stroke-dasharray="80 107" transform="rotate(-90 48 62)"/>
      <circle cx="107" cy="62" r="17" stroke="#eee"/><circle cx="107" cy="62" r="17" stroke="var(--red)" stroke-dasharray="90 107" transform="rotate(-90 107 62)"/>
      <circle cx="168" cy="62" r="17" stroke="#eee"/><circle cx="168" cy="62" r="17" stroke="var(--orange)" stroke-dasharray="70 107" transform="rotate(-90 168 62)"/>
      <circle cx="227" cy="62" r="17" stroke="#eee"/><circle cx="227" cy="62" r="17" stroke="var(--red)" stroke-dasharray="100 107" transform="rotate(-90 227 62)"/>
    </g>
    <g font-size="6" font-weight="700" fill="var(--text)" text-anchor="middle"><text x="48" y="64">2013</text><text x="107" y="64">2014</text><text x="168" y="64">2015</text><text x="227" y="64">2016</text></g>
    <g font-size="6" fill="var(--text)" text-anchor="middle"><text x="48" y="110">157.231</text><text x="107" y="110">257.768</text><text x="168" y="110">312.708</text><text x="227" y="110">514.720</text></g>
    <g stroke="#bbb" stroke-width=".4"><line x1="48" y1="114" x2="48" y2="126"/><line x1="107" y1="114" x2="107" y2="126"/><line x1="168" y1="114" x2="168" y2="126"/><line x1="227" y1="114" x2="227" y2="126"/></g>
    <g font-size="3" font-weight="600" fill="var(--text)" text-anchor="middle"><text x="48" y="133">TITLE HERE</text><text x="107" y="133">TITLE HERE</text><text x="168" y="133">TITLE HERE</text><text x="227" y="133">TITLE HERE</text></g>
    <g font-size="2.3" fill="var(--muted)" text-anchor="middle"><text x="48" y="138">Short line of text here</text><text x="107" y="138">Short line of text here</text><text x="168" y="138">Short line of text here</text><text x="227" y="138">Short line of text here</text></g>
  </svg>
  <footer class="foot"><span class="url">velsori-example.com.tw</span><span class="dot"></span><span class="copy">© 2016 Velsori Biotechnology Inc. › 33</span></footer>
</section>

<!-- 34 Table bar chart -->
<section class="slide">
  <h2 class="slide-title">Table Bar Chart</h2><div class="slide-sub">Your Subtitle Goes Here</div><div class="brand">VELSORI</div>
  <svg class="art" viewBox="0 0 300 168" font-family="Open Sans, sans-serif">
    <g fill="none" stroke="var(--dark)" stroke-width=".6">
      <path d="M28 62 l4 -10 l4 10 z"/><circle cx="32" cy="93" r="4"/><rect x="28" y="121" width="8" height="8"/>
    </g>
    <g font-size="4.4" font-weight="700" fill="var(--text)"><text x="48" y="58">Lorem ipsum</text><text x="48" y="89">Lorem ipsum</text><text x="48" y="120">Lorem ipsum</text></g>
    <g font-size="2.3" fill="var(--muted)"><text x="48" y="63">SHORT NOTE ON THIS ITEM</text><text x="48" y="94">SHORT NOTE ON THIS ITEM</text><text x="48" y="125">SHORT NOTE ON THIS ITEM</text></g>
    <g stroke="#eee" stroke-width=".4"><line x1="150" y1="40" x2="290" y2="40"/><line x1="150" y1="60" x2="290" y2="60"/><line x1="150" y1="80" x2="290" y2="80"/><line x1="150" y1="100" x2="290" y2="100"/><line x1="150" y1="120" x2="290" y2="120"/></g>
    <rect x="156" y="128" width="12" height="20" fill="var(--red)"/><rect x="176" y="92" width="12" height="56" fill="var(--orange)"/>
    <rect x="196" y="64" width="12" height="84" fill="var(--red)"/><rect x="216" y="48" width="12" height="100" fill="var(--orange)"/>
    <rect x="236" y="64" width="12" height="84" fill="var(--red)"/><rect x="256" y="92" width="12" height="56" fill="var(--orange)"/>
    <path d="M162 128 C185 80 205 40 222 44 C240 48 250 80 262 92" fill="none" stroke="var(--red)" stroke-width=".7"/>
    <g font-size="2.2" fill="var(--muted)"><text x="156" y="153">2011</text><text x="176" y="153">2012</text><text x="196" y="153">2013</text><text x="216" y="153">2014</text><text x="236" y="153">2015</text><text x="256" y="153">2016</text></g>
  </svg>
  <footer class="foot"><span class="url">velsori-example.com.tw</span><span class="dot"></span><span class="copy">© 2016 Velsori Biotechnology Inc. › 34</span></footer>
</section>

<!-- 35 Table chart -->
<section class="slide">
  <h2 class="slide-title">Table Chart</h2><div class="slide-sub">Your Subtitle Goes Here</div><div class="brand">VELSORI</div>
  <svg class="art" viewBox="0 0 300 168" font-family="Open Sans, sans-serif">
    <g fill="none" stroke="var(--dark)" stroke-width=".6"><path d="M20 66 l5 -10 l5 10 z"/><circle cx="25" cy="104" r="4.5"/><rect x="20" y="138" width="9" height="9"/></g>
    <g font-size="9" font-weight="700" fill="var(--text)"><text x="38" y="62">$55B</text><text x="38" y="102">$54M</text><text x="38" y="142">$12M</text></g>
    <g font-size="2.4" fill="var(--muted)"><text x="38" y="68">Short line of text here</text><text x="38" y="108">Short line of text here</text><text x="38" y="148">Short line of text here</text></g>
    <text x="151" y="60" font-size="10" font-weight="700" fill="var(--text)">80% GPA</text>
    <g font-size="3" fill="var(--text)"><text x="151" y="68">1)   Northfield Insight</text><text x="151" y="74">2)   Annual Survey of 2016</text></g>
    <g stroke="#eee" stroke-width=".4"><line x1="120" y1="55" x2="280" y2="55"/><line x1="120" y1="80" x2="280" y2="80"/><line x1="120" y1="105" x2="280" y2="105"/><line x1="120" y1="130" x2="280" y2="130"/></g>
    <rect x="132" y="82" width="13" height="66" fill="var(--orange)"/><rect x="158" y="100" width="13" height="48" fill="var(--red)"/>
    <rect x="184" y="86" width="13" height="62" fill="var(--orange)"/><rect x="210" y="70" width="13" height="78" fill="var(--red)"/>
    <rect x="236" y="110" width="13" height="38" fill="var(--red)"/><rect x="262" y="66" width="13" height="82" fill="var(--orange)"/>
    <line x1="120" y1="148" x2="280" y2="148" stroke="#ccc" stroke-width=".4"/>
  </svg>
  <footer class="foot"><span class="url">velsori-example.com.tw</span><span class="dot"></span><span class="copy">© 2016 Velsori Biotechnology Inc. › 35</span></footer>
</section>

<!-- 36 Mobile table chart -->
<section class="slide">
  <h2 class="slide-title">Mobile Table Chart</h2><div class="slide-sub">Your Subtitle Goes Here</div><div class="brand">VELSORI</div>
  <p class="tx" style="left:198px;top:36px;width:92px">Our team builds each step with care, from early cell line work to final fill, so clients move from trial to market with one steady partner.</p>
  <svg class="art" viewBox="0 0 300 168" font-family="Open Sans, sans-serif">
    <g fill="#ececec">
      <rect x="28" y="90" width="5" height="50"/><rect x="38" y="70" width="5" height="70"/><rect x="48" y="98" width="5" height="42"/><rect x="58" y="84" width="5" height="56"/><rect x="68" y="104" width="5" height="36"/><rect x="78" y="80" width="5" height="60"/><rect x="88" y="92" width="5" height="48"/><rect x="98" y="76" width="5" height="64"/><rect x="108" y="100" width="5" height="40"/><rect x="118" y="86" width="5" height="54"/>
      <rect x="188" y="96" width="5" height="44"/><rect x="198" y="84" width="5" height="56"/><rect x="208" y="104" width="5" height="36"/><rect x="218" y="90" width="5" height="50"/><rect x="228" y="78" width="5" height="62"/><rect x="238" y="100" width="5" height="40"/><rect x="248" y="88" width="5" height="52"/><rect x="258" y="94" width="5" height="46"/><rect x="268" y="82" width="5" height="58"/>
    </g>
    <rect x="130" y="42" width="52" height="112" rx="4" fill="#fff" stroke="#cfcfcf" stroke-width="1.5"/>
    <g><rect x="135" y="88" width="5" height="52" fill="var(--orange)"/><rect x="143" y="96" width="5" height="44" fill="var(--orange)"/><rect x="151" y="70" width="5" height="70" fill="var(--red)"/><rect x="159" y="78" width="5" height="62" fill="var(--red)"/><rect x="167" y="60" width="5" height="80" fill="var(--orange)"/><rect x="175" y="100" width="4" height="40" fill="var(--red)"/></g>
    <g font-size="2.2" fill="var(--muted)"><text x="28" y="146">AB CD EF GH IJ KL MN OP QR ST</text><text x="188" y="146">UV WX YZ AB CD EF GH IJ KL</text></g>
  </svg>
  <footer class="foot"><span class="url">velsori-example.com.tw</span><span class="dot"></span><span class="copy">© 2016 Velsori Biotechnology Inc. › 36</span></footer>
</section>

<!-- 37 Graphical chart -->
<section class="slide">
  <h2 class="slide-title">Graphical Chart</h2><div class="slide-sub">Your Subtitle Goes Here</div><div class="brand">VELSORI</div>
  <svg class="art" viewBox="0 0 300 168" font-family="Open Sans, sans-serif">
    <path d="M15 110 L15 92 L30 78 L45 96 L62 70 L80 104 L98 82 L115 96 L135 74 L152 100 L172 72 L190 60 L190 110 Z" fill="var(--orange)"/>
    <path d="M15 110 L15 100 L35 92 L55 104 L75 90 L95 100 L115 88 L140 102 L165 90 L190 98 L190 110 Z" fill="#e0e0e0" opacity=".9"/>
    <g font-size="2.2" fill="var(--muted)"><text x="15" y="115">2001   2002   2003   2004   2005   2006   2007   2008   2009   2010</text></g>
    <g font-size="2.2" fill="var(--text)"><text x="150" y="55">■ Type 1   ■ Type 2</text></g>
    <g font-size="9" fill="var(--text)"><text x="15" y="135">207</text><text x="60" y="135">457+</text><text x="110" y="135">122</text><text x="153" y="135">87+</text></g>
    <g font-size="3" font-weight="600" fill="var(--text)"><text x="15" y="142">TITLE HERE</text><text x="60" y="142">TITLE HERE</text><text x="110" y="142">TITLE HERE</text><text x="153" y="142">TITLE HERE</text></g>
  </svg>
  <div class="photo" role="img" aria-label="Hand holding a smartphone showing the company name" style="left:198px;top:34px;width:94px;height:124px;background:linear-gradient(160deg,#f4f4f4,#d9c3b0)"></div>
  <footer class="foot"><span class="url">velsori-example.com.tw</span><span class="dot"></span><span class="copy">© 2016 Velsori Biotechnology Inc. › 37</span></footer>
</section>

<!-- 38 Comparison chart -->
<section class="slide">
  <h2 class="slide-title">Comparison Chart</h2><div class="slide-sub">Your Subtitle Goes Here</div><div class="brand">VELSORI</div>
  <svg class="art" viewBox="0 0 300 168" font-family="Open Sans, sans-serif">
    <g stroke="#eee" stroke-width=".4"><line x1="30" y1="45" x2="30" y2="105"/><line x1="160" y1="45" x2="160" y2="105"/></g>
    <rect x="30" y="50" width="80" height="4" fill="var(--red)"/><rect x="30" y="56" width="100" height="4" fill="var(--orange)"/><rect x="30" y="62" width="60" height="4" fill="var(--red)"/>
    <rect x="30" y="78" width="90" height="4" fill="var(--red)"/><rect x="30" y="84" width="70" height="4" fill="var(--orange)"/><rect x="30" y="90" width="100" height="4" fill="var(--red)"/>
    <rect x="160" y="48" width="65" height="4" fill="var(--orange)"/><rect x="160" y="54" width="100" height="4" fill="var(--red)"/><rect x="160" y="60" width="80" height="4" fill="var(--orange)"/>
    <rect x="160" y="76" width="95" height="4" fill="var(--orange)"/><rect x="160" y="82" width="70" height="4" fill="var(--red)"/><rect x="160" y="88" width="90" height="4" fill="var(--orange)"/>
    <g font-size="2.2" fill="var(--muted)"><text x="14" y="58">Series 1</text><text x="14" y="86">Series 2</text><text x="145" y="56">Series 3</text><text x="145" y="84">Series 4</text>
      <text x="45" y="112">■ Series 1  ■ Series 2  ■ Series 3</text><text x="175" y="112">■ Series 1  ■ Series 2  ■ Series 3</text></g>
    <g font-size="4.4" font-weight="700" fill="var(--text)"><text x="46" y="133">Lorem ipsum</text><text x="135" y="133">Lorem ipsum</text><text x="227" y="133">Lorem ipsum</text></g>
    <g font-size="2.3" fill="var(--muted)"><text x="46" y="138">SHORT NOTE ON THIS ITEM</text><text x="135" y="138">SHORT NOTE ON THIS ITEM</text><text x="227" y="138">SHORT NOTE ON THIS ITEM</text></g>
  </svg>
  <footer class="foot"><span class="url">velsori-example.com.tw</span><span class="dot"></span><span class="copy">© 2016 Velsori Biotechnology Inc. › 38</span></footer>
</section>

<!-- 39 Revenue charts -->
<section class="slide">
  <h2 class="slide-title">Revenue Charts</h2><div class="slide-sub">Your Subtitle Goes Here</div><div class="brand">VELSORI</div>
  <svg class="art" viewBox="0 0 300 168" font-family="Open Sans, sans-serif">
    <g stroke="#eee" stroke-width=".4"><line x1="25" y1="45" x2="155" y2="45"/><line x1="25" y1="60" x2="155" y2="60"/><line x1="25" y1="75" x2="155" y2="75"/><line x1="25" y1="90" x2="155" y2="90"/><line x1="25" y1="105" x2="155" y2="105"/><line x1="25" y1="120" x2="155" y2="120"/><line x1="25" y1="135" x2="155" y2="135"/></g>
    <g stroke="#999" stroke-width=".4"><line x1="40" y1="68" x2="40" y2="110"/><line x1="66" y1="76" x2="66" y2="116"/><line x1="90" y1="60" x2="90" y2="96"/><line x1="115" y1="64" x2="115" y2="100"/><line x1="140" y1="80" x2="140" y2="120"/></g>
    <rect x="36" y="76" width="8" height="22" fill="var(--red)"/><rect x="62" y="86" width="8" height="14" fill="var(--orange)"/><rect x="86" y="68" width="8" height="14" fill="var(--orange)"/><rect x="111" y="70" width="8" height="18" fill="var(--red)"/><rect x="136" y="88" width="8" height="18" fill="var(--red)"/>
    <g font-size="2.4" fill="var(--muted)"><text x="68" y="142">Open    High    Low    Close</text></g>
    <g fill="none" stroke-width="3.5">
      <circle cx="194" cy="66" r="18" stroke="#eee"/><circle cx="194" cy="66" r="18" stroke="var(--red)" stroke-dasharray="85 113" transform="rotate(-90 194 66)"/>
      <circle cx="252" cy="66" r="18" stroke="#eee"/><circle cx="252" cy="66" r="18" stroke="var(--orange)" stroke-dasharray="70 113" transform="rotate(-90 252 66)"/>
    </g>
    <g font-size="6" font-weight="700" fill="var(--text)" text-anchor="middle"><text x="194" y="68">2015</text><text x="252" y="68">2016</text></g>
    <g font-size="6" fill="var(--text)" text-anchor="middle"><text x="194" y="108">382.146</text><text x="252" y="108">382.146</text></g>
    <g font-size="3" font-weight="600" fill="var(--text)" text-anchor="middle"><text x="194" y="130">Revenue</text><text x="252" y="130">Revenue</text></g>
    <g font-size="2.3" fill="var(--muted)" text-anchor="middle"><text x="194" y="135">Short line of text here</text><text x="252" y="135">Short line of text here</text></g>
  </svg>
  <footer class="foot"><span class="url">velsori-example.com.tw</span><span class="dot"></span><span class="copy">© 2016 Velsori Biotechnology Inc. › 39</span></footer>
</section>

<!-- 40 Radar infographic -->
<section class="slide">
  <h2 class="slide-title">Radar Infographic</h2><div class="slide-sub">Your Subtitle Goes Here</div><div class="brand">VELSORI</div>
  <svg class="art" viewBox="0 0 300 168" font-family="Open Sans, sans-serif">
    <circle cx="150" cy="100" r="45" fill="none" stroke="#ddd" stroke-width=".6"/>
    <g stroke="#eee" stroke-width=".4"><line x1="150" y1="55" x2="150" y2="145"/><line x1="111" y1="77" x2="189" y2="123"/><line x1="111" y1="123" x2="189" y2="77"/></g>
    <path d="M150 72 C165 62 182 70 178 86 C176 100 172 112 162 124 C155 134 146 134 140 124 C130 110 122 96 126 84 C130 70 140 74 150 72 Z" fill="none" stroke="var(--orange)" stroke-width="1.2"/>
    <g font-size="4.2" fill="var(--text)"><text x="144" y="52">47%</text><text x="95" y="78">71%</text><text x="194" y="78">79%</text><text x="95" y="127">63%</text><text x="194" y="127">54%</text><text x="144" y="155">89%</text></g>
    <g font-size="4.4" font-weight="700" fill="var(--text)"><text x="33" y="60">Lorem ipsum</text><text x="33" y="91">Lorem ipsum</text><text x="33" y="122">Lorem ipsum</text><text x="215" y="60">Lorem ipsum</text><text x="215" y="91">Lorem ipsum</text><text x="215" y="122">Lorem ipsum</text></g>
    <g font-size="2.3" fill="var(--muted)"><text x="33" y="65">SHORT NOTE ON THIS ITEM</text><text x="33" y="96">SHORT NOTE ON THIS ITEM</text><text x="33" y="127">SHORT NOTE ON THIS ITEM</text><text x="215" y="65">SHORT NOTE ON THIS ITEM</text><text x="215" y="96">SHORT NOTE ON THIS ITEM</text><text x="215" y="127">SHORT NOTE ON THIS ITEM</text></g>
  </svg>
  <footer class="foot"><span class="url">velsori-example.com.tw</span><span class="dot"></span><span class="copy">© 2016 Velsori Biotechnology Inc. › 40</span></footer>
</section>

<!-- 41 Half circle chart -->
<section class="slide">
  <h2 class="slide-title">Half Circle Chart</h2><div class="slide-sub">Your Subtitle Goes Here</div><div class="brand">VELSORI</div>
  <svg class="art" viewBox="0 0 300 168" font-family="Open Sans, sans-serif">
    <path d="M232 40 A48 48 0 0 1 232 136" fill="none" stroke="var(--orange)" stroke-width="7"/>
    <path d="M232 50 A38 38 0 0 1 232 126" fill="none" stroke="#ececec" stroke-width="5"/>
    <path d="M232 50 A38 38 0 0 1 262 110" fill="none" stroke="var(--red)" stroke-width="5"/>
    <path d="M232 60 A28 28 0 0 1 232 116" fill="none" stroke="#ececec" stroke-width="4"/>
    <g font-size="3" fill="var(--muted)"><text x="200" y="88">55%</text><text x="200" y="109">78%</text><text x="210" y="122">63%</text><text x="274" y="139">85%</text></g>
    <g fill="none" stroke="#999" stroke-width=".4">
      <polyline points="52,68 52,56 232,56"/><polyline points="95,90 95,66 232,66"/><polyline points="138,104 138,78 215,78"/><polyline points="180,126 180,96 215,96"/>
    </g>
    <g font-size="3" font-weight="600" fill="var(--text)"><text x="25" y="73">Content A</text><text x="66" y="95">Content B</text><text x="110" y="109">Content C</text><text x="154" y="131">Content D</text></g>
    <g font-size="2.3" fill="var(--muted)"><text x="25" y="77">Short line of text here</text><text x="66" y="99">Short line of text here</text><text x="110" y="113">Short line of text here</text><text x="154" y="135">Short line of text here</text></g>
  </svg>
  <footer class="foot"><span class="url">velsori-example.com.tw</span><span class="dot"></span><span class="copy">© 2016 Velsori Biotechnology Inc. › 41</span></footer>
</section>

<!-- 42 Table content -->
<section class="slide">
  <h2 class="slide-title">Table Content</h2><div class="slide-sub">Your Subtitle Goes Here</div><div class="brand">VELSORI</div>
  <h3 class="hd" style="left:16px;top:35px;font-size:3.4px">Lorem ipsum dolor sit amet</h3>
  <p class="tx" style="left:16px;top:42px;width:140px">Our team builds each step with care, from early cell line work to final fill, so clients move from trial to market with one steady partner. Clear methods and tested systems keep each batch on track and ready for review.</p>
  <svg class="art" viewBox="0 0 300 168" font-family="Open Sans, sans-serif">
    <g font-size="2.4" fill="var(--muted)"><text x="210" y="42">Title Goes Here</text><text x="75" y="90">Title Goes Here</text></g>
    <g font-size="2.2" fill="var(--muted)"><text x="193" y="50">Q1</text><text x="215" y="50">Q2</text><text x="237" y="50">Q3</text><text x="259" y="50">Q4</text>
      <text x="163" y="57">ACTIVITY 1</text><text x="163" y="67">ACTIVITY 2</text><text x="163" y="77">ACTIVITY 3</text><text x="163" y="87">ACTIVITY 4</text></g>
    <g fill="#e4e4e4" stroke="#fff" stroke-width=".6">
      <rect x="183" y="52" width="22" height="10"/><rect x="205" y="52" width="22" height="10"/><rect x="227" y="52" width="22" height="10"/><rect x="249" y="52" width="22" height="10"/>
      <rect x="183" y="62" width="22" height="10"/><rect x="205" y="62" width="22" height="10"/><rect x="227" y="62" width="22" height="10"/><rect x="249" y="62" width="22" height="10"/>
      <rect x="183" y="72" width="22" height="10"/><rect x="205" y="72" width="22" height="10"/><rect x="227" y="72" width="22" height="10"/><rect x="249" y="72" width="22" height="10"/>
      <rect x="183" y="82" width="22" height="10"/><rect x="205" y="82" width="22" height="10"/><rect x="227" y="82" width="22" height="10"/><rect x="249" y="82" width="22" height="10"/>
    </g>
    <rect x="183" y="52" width="22" height="10" fill="var(--red)"/><rect x="205" y="62" width="22" height="10" fill="var(--orange)"/><rect x="227" y="72" width="22" height="10" fill="var(--red)"/><rect x="205" y="72" width="22" height="10" fill="var(--orange)"/><rect x="249" y="82" width="22" height="10" fill="var(--orange)"/>
    <g font-size="2.2" fill="var(--muted)"><text x="50" y="98">Q1</text><text x="72" y="98">Q2</text><text x="94" y="98">Q3</text><text x="116" y="98">Q4</text>
      <text x="20" y="105">ACTIVITY 1</text><text x="20" y="115">ACTIVITY 2</text><text x="20" y="125">ACTIVITY 3</text><text x="20" y="135">ACTIVITY 4</text></g>
    <g fill="#e4e4e4" stroke="#fff" stroke-width=".6">
      <rect x="42" y="100" width="22" height="10"/><rect x="64" y="100" width="22" height="10"/><rect x="86" y="100" width="22" height="10"/><rect x="108" y="100" width="22" height="10"/>
      <rect x="42" y="110" width="22" height="10"/><rect x="64" y="110" width="22" height="10"/><rect x="86" y="110" width="22" height="10"/><rect x="108" y="110" width="22" height="10"/>
      <rect x="42" y="120" width="22" height="10"/><rect x="64" y="120" width="22" height="10"/><rect x="86" y="120" width="22" height="10"/><rect x="108" y="120" width="22" height="10"/>
      <rect x="42" y="130" width="22" height="10"/><rect x="64" y="130" width="22" height="10"/><rect x="86" y="130" width="22" height="10"/><rect x="108" y="130" width="22" height="10"/>
    </g>
    <rect x="42" y="100" width="22" height="10" fill="var(--orange)"/><rect x="64" y="110" width="22" height="10" fill="var(--red)"/><rect x="64" y="120" width="22" height="10" fill="var(--red)"/><rect x="86" y="120" width="22" height="10" fill="var(--orange)"/><rect x="108" y="130" width="22" height="10" fill="var(--orange)"/>
    <g font-size="2.3" fill="var(--muted)"><text x="160" y="110">✔ Check this item</text><text x="160" y="115">✔ Check this item</text><text x="160" y="120">✔ Check this item</text><text x="160" y="125">✔ Check this item</text><text x="160" y="130">✔ Check this item</text>
      <text x="222" y="110">✔ Check this item</text><text x="222" y="115">✔ Check this item</text><text x="222" y="120">✔ Check this item</text><text x="222" y="125">✔ Check this item</text><text x="222" y="130">✔ Check this item</text></g>
  </svg>
  <footer class="foot"><span class="url">velsori-example.com.tw</span><span class="dot"></span><span class="copy">© 2016 Velsori Biotechnology Inc. › 42</span></footer>
</section>

<!-- 43 Table bar chart / data analysis -->
<section class="slide">
  <h2 class="slide-title">Table Bar Chart</h2><div class="slide-sub">Your Subtitle Goes Here</div><div class="brand">VELSORI</div>
  <h3 class="hd" style="left:20px;top:48px;font-size:4px;font-weight:600">Data Analysis</h3>
  <p class="tx" style="left:20px;top:56px;width:75px">Our team builds each step with care, from early cell line work to final fill, so clients move from trial to market with one steady partner at every stage of work.</p>
  <p class="tx" style="left:20px;top:90px;width:75px">• Clear methods for each run<br>• Tested systems and steady care<br>• Results shared in plain terms<br>• Every batch logged and checked</p>
  <svg class="art" viewBox="0 0 300 168" font-family="Open Sans, sans-serif">
    <g><rect x="107" y="120" width="4" height="26" fill="var(--orange)"/><rect x="112" y="126" width="4" height="20" fill="var(--orange)"/><rect x="117" y="110" width="4" height="36" fill="var(--red)"/><rect x="122" y="72" width="4" height="74" fill="var(--red)"/></g>
    <g><rect x="152" y="72" width="4" height="74" fill="var(--orange)"/><rect x="157" y="104" width="4" height="42" fill="var(--orange)"/><rect x="162" y="92" width="4" height="54" fill="var(--orange)"/><rect x="167" y="124" width="4" height="22" fill="var(--orange)"/></g>
    <g><rect x="197" y="118" width="4" height="28" fill="var(--red)"/><rect x="202" y="126" width="4" height="20" fill="var(--orange)"/><rect x="207" y="100" width="4" height="46" fill="var(--red)"/><rect x="212" y="74" width="4" height="72" fill="var(--red)"/></g>
    <g><rect x="242" y="128" width="4" height="18" fill="var(--orange)"/><rect x="247" y="136" width="4" height="10" fill="var(--orange)"/><rect x="252" y="72" width="4" height="74" fill="var(--orange)"/><rect x="257" y="110" width="4" height="36" fill="var(--red)"/></g>
    <line x1="104" y1="146" x2="265" y2="146" stroke="#ccc" stroke-width=".4"/>
    <g font-size="3" fill="var(--text)"><text x="106" y="153">Bar Chart 01</text><text x="151" y="153">Bar Chart 02</text><text x="196" y="153">Bar Chart 03</text><text x="241" y="153">Bar Chart 04</text></g>
  </svg>
  <footer class="foot"><span class="url">velsori-example.com.tw</span><span class="dot"></span><span class="copy">© 2016 Velsori Biotechnology Inc. › 43</span></footer>
</section>

<!-- 44 Client testimonials -->
<section class="slide">
  <h2 class="slide-title">Client Testimonials</h2><div class="slide-sub">Your Subtitle Goes Here</div><div class="brand">VELSORI</div>
  <svg class="art" viewBox="0 0 300 168" font-family="Open Sans, sans-serif">
    <g text-anchor="middle"><text x="150" y="40" font-size="3" fill="var(--muted)">Client Testimonial</text>
      <text x="150" y="47" font-size="3.2" font-weight="700" fill="var(--text)">WHAT OUR CLIENT SAYS</text>
      <text x="150" y="54" font-size="4" fill="var(--orange)">★★★★☆</text>
      <text x="150" y="59" font-size="2.2" fill="var(--muted)">CLIENT RATING</text>
      <text x="150" y="76" font-size="3.2" fill="var(--text)">Working with this team kept our program on time, our data clean and our</text>
      <text x="150" y="81" font-size="3.2" fill="var(--text)">questions answered quickly, from the first batch to the final</text>
      <text x="150" y="86" font-size="3.2" fill="var(--text)">report, with steady care.</text>
      <text x="150" y="132" font-size="2.2" fill="var(--muted)">CLIENT NAME HERE</text></g>
    <text x="95" y="76" font-size="12" fill="var(--text)">“</text><text x="200" y="92" font-size="12" fill="var(--text)">”</text>
  </svg>
  <div class="avatar" role="img" aria-label="Client portrait" style="left:139px;top:104px;width:22px;height:22px"></div>
  <footer class="foot"><span class="url">velsori-example.com.tw</span><span class="dot"></span><span class="copy">© 2016 Velsori Biotechnology Inc. › 44</span></footer>
</section>

<!-- 45 Leadership -->
<section class="slide">
  <h2 class="slide-title">Leadership</h2><div class="slide-sub">Quotes Here</div><div class="brand">VELSORI</div>
  <svg class="art" viewBox="0 0 300 168" font-family="Open Sans, sans-serif">
    <g fill="#fff" stroke="#d6d6d6" stroke-width=".5"><rect x="28" y="45" width="80" height="65"/><rect x="114" y="45" width="80" height="65"/><rect x="200" y="45" width="80" height="65"/></g>
    <g font-size="2.5" fill="var(--muted)">
      <text x="33" y="54">Working with this team kept our program</text><text x="33" y="58">on time and our data clean, from the first</text><text x="33" y="62">batch to the last report, with clear notes</text><text x="33" y="66">and steady care at every single stage.</text>
      <text x="119" y="54">Working with this team kept our program</text><text x="119" y="58">on time and our data clean, from the first</text><text x="119" y="62">batch to the last report, with clear notes</text><text x="119" y="66">and steady care at every single stage.</text>
      <text x="205" y="54">Working with this team kept our program</text><text x="205" y="58">on time and our data clean, from the first</text><text x="205" y="62">batch to the last report, with clear notes</text><text x="205" y="66">and steady care at every single stage.</text>
      <text x="33" y="92">VP of Product Strategy</text><text x="119" y="92">Marketing</text><text x="205" y="92">VP of Operations</text>
    </g>
    <g font-size="3.4" fill="var(--text)"><text x="33" y="87">PERSON NAME</text><text x="119" y="87">PERSON NAME</text><text x="205" y="87">PERSON NAME</text></g>
    <g font-size="14" font-weight="700" fill="var(--orange)"><text x="92" y="98">”</text><text x="178" y="98">”</text><text x="264" y="98">”</text></g>
  </svg>
  <div class="avatar" role="img" aria-label="Leader portrait" style="left:82px;top:122px;width:20px;height:20px"></div>
  <div class="avatar" role="img" aria-label="Leader portrait" style="left:168px;top:122px;width:20px;height:20px"></div>
  <div class="avatar" role="img" aria-label="Leader portrait" style="left:254px;top:122px;width:20px;height:20px"></div>
  <footer class="foot"><span class="url">velsori-example.com.tw</span><span class="dot"></span><span class="copy">© 2016 Velsori Biotechnology Inc. › 45</span></footer>
</section>

<!-- 46 Quote with photo -->
<section class="slide">
  <div class="photo" role="img" aria-label="Scientist's gloved hand tending a seedling in a lab beside a glass beaker" style="inset:0;background:linear-gradient(120deg,#6d5a44,#a89478 45%,#4f5a3a)"></div>
  <svg class="art" viewBox="0 0 300 168" font-family="Open Sans, sans-serif">
    <polygon points="145,168 300,0 300,168" fill="var(--orange)" opacity=".92"/>
    <polygon points="200,0 300,0 300,110" fill="var(--orange)" opacity=".55"/>
    <text x="258" y="62" font-size="34" font-weight="700" fill="#fff">”</text>
    <g font-size="7" font-weight="300" fill="#fff" text-anchor="end">
      <text x="285" y="76">The point of using</text><text x="285" y="88">Lorem Ipsum is that it</text><text x="285" y="100">has a more-or-less</text><text x="285" y="112">normal distribution of</text><text x="285" y="124">letters.</text>
    </g>
    <text x="285" y="138" font-size="5" font-weight="700" fill="#fff" text-anchor="end">- VELSORI BIOTECH</text>
  </svg>
</section>

<!-- 47 Meet our team -->
<section class="slide">
  <h2 class="slide-title">Meet Our Team</h2><div class="slide-sub">Your Subtitle Goes Here</div><div class="brand">VELSORI</div>
  <div class="avatar" role="img" aria-label="Team member portrait" style="left:40px;top:52px;width:38px;height:38px"></div>
  <div class="avatar" role="img" aria-label="Team member portrait" style="left:99px;top:52px;width:38px;height:38px"></div>
  <div class="avatar" role="img" aria-label="Team member portrait" style="left:163px;top:52px;width:38px;height:38px"></div>
  <div class="avatar" role="img" aria-label="Team member portrait" style="left:218px;top:52px;width:38px;height:38px"></div>
  <svg class="art" viewBox="0 0 300 168" font-family="Open Sans, sans-serif">
    <g font-size="4" font-weight="600" fill="var(--text)" text-anchor="middle"><text x="59" y="102">MIRELA VOSS</text><text x="118" y="102">OWEN TALBRIK</text><text x="182" y="102">SILAS KOREN</text><text x="237" y="102">DARIO MENTH</text></g>
    <g font-size="2.5" fill="var(--muted)" text-anchor="middle">
      <text x="59" y="109">A short note on this</text><text x="59" y="113">person and their role</text>
      <text x="118" y="109">A short note on this</text><text x="118" y="113">person and their role</text>
      <text x="182" y="109">A short note on this</text><text x="182" y="113">person and their role</text>
      <text x="237" y="109">A short note on this</text><text x="237" y="113">person and their role</text>
    </g>
    <g fill="var(--muted)"><circle cx="54" cy="122" r="1.2"/><circle cx="59" cy="122" r="1.2"/><circle cx="64" cy="122" r="1.2"/><circle cx="113" cy="122" r="1.2"/><circle cx="118" cy="122" r="1.2"/><circle cx="123" cy="122" r="1.2"/><circle cx="177" cy="122" r="1.2"/><circle cx="182" cy="122" r="1.2"/><circle cx="187" cy="122" r="1.2"/><circle cx="232" cy="122" r="1.2"/><circle cx="237" cy="122" r="1.2"/><circle cx="242" cy="122" r="1.2"/></g>
  </svg>
  <footer class="foot"><span class="url">velsori-example.com.tw</span><span class="dot"></span><span class="copy">© 2016 Velsori Biotechnology Inc. › 47</span></footer>
</section>

<!-- Contact -->
<section class="slide contact">
  <div class="top"></div>
  <svg class="art" viewBox="0 0 300 168" font-family="Open Sans, sans-serif">
    <g text-anchor="middle" fill="#fff">
      <text x="150" y="47" font-size="6.5" font-weight="600">Lumeta Biotechnology Co., Ltd</text>
      <text x="150" y="56" font-size="3.4">Harbor Science Road,</text>
      <text x="150" y="61" font-size="3.4">Zhubei District, Lane 42</text>
    </g>
    <g fill="none" stroke="#fff" stroke-width=".5"><circle cx="125" cy="70" r="3.3"/><circle cx="142" cy="70" r="3.3"/><circle cx="159" cy="70" r="3.3"/><circle cx="176" cy="70" r="3.3"/></g>
    <path d="M147 104 q1 -2 2.5 -1 l1.5 1.5 q.5 1 -.5 1.5 q1 2 3 3 q.5 -1 1.5 -.5 l1.5 1.5 q1 1.5 -1 2.5 q-5 0 -8.5 -8.5 z" fill="none" stroke="#ccc" stroke-width=".5"/>
    <g text-anchor="middle" fill="#fff"><text x="150" y="125" font-size="7.5">555.014.2270</text><text x="150" y="149" font-size="4">media@velsori-example.com.tw</text></g>
    <rect x="147" y="133" width="6" height="7" fill="none" stroke="#ccc" stroke-width=".5"/>
  </svg>
</section>

<!-- Global locations -->
<section class="slide mapslide">
  <div class="photo" role="img" aria-label="World map with highlighted countries in orange, red, green and blue" style="left:0;top:0;width:300px;height:168px;background:radial-gradient(ellipse at 55% 45%,#6a6a6a,#4a4a4a 70%)"></div>
  <svg class="art" viewBox="0 0 300 168" font-family="Open Sans, sans-serif">
    <text x="12" y="128" font-size="11" font-weight="700" fill="#fff">Global</text>
    <text x="12" y="141" font-size="11" font-weight="300" fill="#fff">Locations</text>
  </svg>
</section>

<section class="slide blank" aria-hidden="true"></section>

</main>
</body>
</html>
```